Quillstone Restaurnt Lunch Menu Redesign:

We have two lunch special menus that need to be reformatted into a 4.25inx11in and need a graphics design update. Some menu items need to change and some descriptions need to updated. This new menu should double sided with the Main Dining Lunch Menu on the front side and Teppanyaki Lunch menu on the back.

Both menus should follow the same design formatting as the main dining lunch menu (font, sizing, ect.)

```html
<!DOCTYPE html>
<html lang="en">
<head>
<meta charset="utf-8">
<title>Quillstone Lunch Menus</title>
<link href="https://fonts.googleapis.com/css2?family=Playfair+Display:wght@500;600&family=Great+Vibes&family=Poppins:wght@400;500;600;700&display=swap" rel="stylesheet">
<style>
  :root{
    --stage:#8f8f8f;
    --paper:#f8f8f8;
    --paper-edge:#f1f1f1;
    --ink:#111111;
    --ink-soft:#3a3a3a;
    --rule:#9a9a9a;
    --leader:#b8b8b8;
    --band:#000000;
    --band-text:#ffffff;
  }
  *{box-sizing:border-box;margin:0;padding:0}
  html,body{width:1200px;height:1198px;overflow:hidden}
  body{background:var(--stage);position:relative;font-family:"Poppins",sans-serif;color:var(--ink)}

  .menu-card{position:absolute;top:124px;height:950px;background:linear-gradient(180deg,var(--paper),var(--paper-edge));overflow:hidden}
  .menu-card--main{left:174px;width:348px}
  .menu-card--teppan{left:642px;width:368px}
  .paper-texture{position:absolute;inset:0}

  .block{position:absolute;left:31px;right:28px}
  .menu-card--teppan .block{left:32px;right:32px}

  .title{font-family:"Playfair Display",serif;font-weight:600;text-align:center;line-height:1;letter-spacing:3px}
  .title--lunch{top:28px;font-size:58px}
  .title--teppan{top:33px;font-size:40px;letter-spacing:2.5px}
  .script{font-family:"Great Vibes",cursive;text-align:center;line-height:1;font-size:32px}
  .script--specials{top:84px}
  .script--teppan{top:86px}

  .service-bar{border-top:1px solid var(--rule);border-bottom:1px solid var(--rule);text-align:center;font-weight:600;font-size:13.5px;line-height:27px}
  .service-bar--main{top:131px;height:29px;left:37px;right:37px}
  .service-bar--teppan{top:133px;height:31px;line-height:29px}
  .service-bar span+span{margin-left:14px}

  .section-head{font-family:"Playfair Display",serif;font-weight:500;font-size:15.5px;letter-spacing:0.2px;line-height:1}
  .note-box{border:1px solid var(--ink-soft);font-size:9px;line-height:11.5px;padding:4px 9px;color:var(--ink-soft)}

  .item{display:flex;justify-content:space-between;font-size:9.5px;line-height:11.5px}
  .item-name{font-weight:700}
  .item-desc{font-size:9px;color:var(--ink-soft);line-height:11px}
  .price{font-family:"Playfair Display",serif;font-size:9.5px}
  .price sup{font-size:6px;vertical-align:4px}

  .sandwich-list .entry{height:30px}
  .main-list .entry{min-height:15.6px}

  .sushi-grid{display:grid;grid-template-columns:173px 1fr;font-size:9px;line-height:14.4px}
  .sushi-grid b{font-weight:700}

  .footer-band{position:absolute;left:0;right:0;top:893px;height:57px;background:var(--band);color:var(--band-text);font-size:7.6px;line-height:9.6px;padding:8px 31px}

  .price-list .row{display:flex;align-items:baseline;height:21.6px;font-size:9px;font-weight:600}
  .price-list .leader{flex:1;border-bottom:1.5px dotted var(--leader);margin:0 6px;transform:translateY(-2px)}

  .special-frame{position:absolute;left:32px;right:32px;top:569px;height:351px;border:1px solid var(--ink-soft)}
  .special-frame .spark{position:absolute;font-size:11px;line-height:1}
  .special-title{position:absolute;left:0;right:0;top:20px;font-family:"Playfair Display",serif;font-weight:600;font-size:40px;text-align:center;letter-spacing:3px;line-height:1}
  .special-script{position:absolute;left:0;right:0;top:62px;font-family:"Great Vibes",cursive;font-size:32px;text-align:center;line-height:1}
  .special-rule{position:absolute;left:16px;right:16px;top:119px;border-top:1px solid var(--rule)}
  .special-note{position:absolute;left:16px;right:16px;top:131px;height:51px;text-align:center;padding:5px 10px}
  .special-note strong{font-weight:600;color:var(--ink)}
  .special-frame .price-list{position:absolute;left:16px;right:16px;top:196px}
</style>
</head>
<body>

<section class="menu-card menu-card--main" aria-label="Main dining lunch specials">
  <div class="paper-texture" role="img" aria-label="Light grey wave pattern background"></div>

  <h1 class="block title title--lunch">LUNCH</h1>
  <p class="block script script--specials">Specials</p>
  <p class="block service-bar service-bar--main"><span>Served Daily</span><span>11AM - 3PM</span></p>

  <h2 class="block section-head" style="top:191px">SANDWICHES</h2>
  <p class="block note-box" style="top:216px;height:32px;right:118px;padding-top:3px">Served with Choice of Miso Soup or House Salad &amp; Potato Chips</p>
  <div class="block sandwich-list" style="top:259px">
    <div class="entry"><div class="item"><span class="item-name">Fried Breaded Calamari Steak</span><span class="price"><sup>$</sup>16</span></div><div class="item-desc">With Tomato, Lettuce &amp; Onion</div></div>
    <div class="entry"><div class="item"><span class="item-name">Grilled Chicken</span><span class="price"><sup>$</sup>16</span></div><div class="item-desc">With Bacon, Tomato, Lettuce &amp; Mayonnaise Drizzle</div></div>
    <div class="entry"><div class="item"><span class="item-name">Hamburger</span><span class="price"><sup>$</sup>18</span></div><div class="item-desc">With Lettuce, Tomato, Onion, Mayonnaise Drizzle</div></div>
    <div class="entry"><div class="item"><span class="item-name">Fried Soft Shell Crab Burger</span><span class="price"><sup>$</sup>20</span></div><div class="item-desc">With Avocado, Lettuce, Tomato, Onion &amp; Mayo</div></div>
  </div>

  <h2 class="block section-head" style="top:403px">SUSHI SPECIALS</h2>
  <div class="block note-box" style="top:428px;height:48px;right:36px">
    <p>Please Select 4 of the followings for &nbsp;&nbsp;&nbsp;&nbsp;&nbsp;<span class="price"><sup>$</sup>16</span></p>
    <p>Served with a 4 piece California Roll &amp; Miso Soup or House Salad</p>
  </div>
  <div class="block sushi-grid" style="top:484px">
    <span><b>Hamachi</b> - Yellowtail Tuna</span><span><b>Maguro</b> - Yellow fin Tuna</span>
    <span><b>Hotate</b> - Scallop</span><span><b>Smoked Salmon</b></span>
    <span><b>Ika</b> - Squid</span><span></span>
    <span><b>Ikura</b> - Salmon Roe</span><span><b>Tako</b> - Octopus</span>
    <span><b>Saba</b> - Mackerel</span><span><b>Unagi</b> - BBQ Eel</span>
    <span><b>Sake</b> - Salmon</span><span><b>Ebi</b> - Shrimp</span>
    <span><b>Tai</b> - Red Snapper</span><span><b>Tamago</b> - Egg</span>
  </div>

  <h2 class="block section-head" style="top:617px">MAIN COURSES</h2>
  <div class="block note-box" style="top:641px;height:32px;right:36px;padding-top:3px">
    <p>Served with Rice &amp; Choice of Miso Soup or House Salad</p>
    <p>All Meals Served with Rice. Upgrade to fried rice for only <span class="price"><sup>$</sup>4</span></p>
  </div>
  <div class="block main-list" style="top:685px">
    <div class="entry"><div class="item"><span class="item-name">Organic Tofu Teriyaki</span><span class="price"><sup>$</sup>14</span></div><div class="item-desc">Served Grilled or Tempura Fried</div></div>
    <div class="entry"><div class="item"><span class="item-name">Chicken Teriyaki</span><span class="price"><sup>$</sup>16</span></div></div>
    <div class="entry"><div class="item"><span class="item-name">Spicy Chicken Teriyaki</span><span class="price"><sup>$</sup>16</span></div></div>
    <div class="entry"><div class="item"><span class="item-name">Beef Teriyaki</span><span class="price"><sup>$</sup>16</span></div></div>
    <div class="entry"><div class="item"><span class="item-name">Spicy Beef Teriyaki</span><span class="price"><sup>$</sup>16</span></div></div>
    <div class="entry"><div class="item"><span class="item-name">Chicken Katsu</span><span class="price"><sup>$</sup>15</span></div><div class="item-desc">Breaded Chicken Breast</div></div>
    <div class="entry"><div class="item"><span class="item-name">Katsu Don</span><span class="price"><sup>$</sup>16</span></div><div class="item-desc" style="font-size:8px">Fried Chicken Breast, Egg &amp; Onion over Rice</div></div>
    <div class="entry"><div class="item"><span class="item-name">Unagi Don</span><span class="price"><sup>$</sup>19</span></div><div class="item-desc">BBQ Eel over Rice</div></div>
    <div class="entry"><div class="item"><span class="item-name">Shrimp &amp; Vegetable Tempura</span><span class="price"><sup>$</sup>16</span></div></div>
  </div>

  <footer class="footer-band">
    <p>Served Raw</p>
    <p>20% gratuity added to parties of 6 or more.</p>
    <p>Consuming raw or undercooked food may increase your risk of foodborne illness</p>
  </footer>
</section>

<section class="menu-card menu-card--teppan" aria-label="Teppanyaki lunch menu">
  <div class="paper-texture" role="img" aria-label="Light grey wave pattern background"></div>

  <h1 class="block title title--teppan">TEPPANYAKI</h1>
  <p class="block script script--teppan">Lunch</p>
  <p class="block service-bar service-bar--teppan">Available until 11-2:30pm</p>
  <p class="block note-box" style="top:184px;height:25px;text-align:center;line-height:15px">Served with Miso Soup or Salad, Choice of Rice &amp; Vegetables</p>

  <div class="block price-list" style="top:223px">
    <div class="row"><span>Hibachi Chicken</span><span class="leader"></span><span class="price"><sup>$</sup>18.00</span></div>
    <div class="row"><span>Hibachi Shrimp</span><span class="leader"></span><span class="price"><sup>$</sup>19.00</span></div>
    <div class="row"><span>Hibachi New York Steak</span><span class="leader"></span><span class="price"><sup>$</sup>20.00</span></div>
    <div class="row"><span>Hibachi Salmon</span><span class="leader"></span><span class="price"><sup>$</sup>20.00</span></div>
    <div class="row"><span>Teriyaki Beef</span><span class="leader"></span><span class="price"><sup>$</sup>19.00</span></div>
    <div class="row"><span>Hibachi Scallop</span><span class="leader"></span><span class="price"><sup>$</sup>20.00</span></div>
    <div class="row"><span>Chicken and Shrimp</span><span class="leader"></span><span class="price"><sup>$</sup>21.00</span></div>
    <div class="row"><span>Scallop and Shrimp</span><span class="leader"></span><span class="price"><sup>$</sup>22.00</span></div>
    <div class="row"><span>New York Steak and Chicken</span><span class="leader"></span><span class="price"><sup>$</sup>22.00</span></div>
    <div class="row"><span>New York Steak and Shrimp</span><span class="leader"></span><span class="price"><sup>$</sup>23.00</span></div>
    <div class="row"><span>New York Steak and Scallop</span><span class="leader"></span><span class="price"><sup>$</sup>24.00</span></div>
    <div class="row"><span>Filet Mignon</span><span class="leader"></span><span class="price"><sup>$</sup>23.00</span></div>
    <div class="row"><span>Filet Mignon and Chicken</span><span class="leader"></span><span class="price"><sup>$</sup>25.00</span></div>
    <div class="row"><span>Filet Mignon and Shrimp</span><span class="leader"></span><span class="price"><sup>$</sup>26.00</span></div>
    <div class="row"><span>Filet Mignon and Scallop</span><span class="leader"></span><span class="price"><sup>$</sup>27.00</span></div>
  </div>

  <div class="special-frame">
    <span class="spark" style="left:40px;top:18px">&#10022;</span>
    <span class="spark" style="right:40px;top:18px">&#10022;</span>
    <h2 class="special-title">SPECIAL</h2>
    <p class="special-script">Menu</p>
    <div class="special-rule"></div>
    <div class="note-box special-note">
      <p><strong>Ages 12 and Under – Ages 65 and Older</strong></p>
      <p>Served with Miso Soup or Salad, Choice of Rice &amp; Vegetables</p>
    </div>
    <div class="price-list">
      <div class="row"><span>Hibachi Chicken</span><span class="leader" style="border:0"></span><span class="price"><sup>$</sup>15.00</span></div>
      <div class="row"><span>Hibachi Shrimp</span><span class="leader" style="border:0"></span><span class="price"><sup>$</sup>16.00</span></div>
      <div class="row"><span>Hibachi Scallop</span><span class="leader" style="border:0"></span><span class="price"><sup>$</sup>18.00</span></div>
      <div class="row"><span>Hibachi New York Steak</span><span class="leader" style="border:0"></span><span class="price"><sup>$</sup>18.00</span></div>
      <div class="row"><span>Hibachi Scallop</span><span class="leader" style="border:0"></span><span class="price"><sup>$</sup>18.00</span></div>
      <div class="row"><span>Teriyaki Beef</span><span class="leader" style="border:0"></span><span class="price"><sup>$</sup>16.00</span></div>
    </div>
  </div>
</section>

</body>
</html>
```